Image Ads needed for a Pharmacy Education e-commerce website

I need image ads with these specifications:

Supported formats: JPG, PNG, GIF
File size: 3MB max
Recommended aspect ratios: 1:1 square; 4:5 portrait; 4:3 landscape; 16:9 landscape
Recommended resolutions: 1080x1080 square, 1080x1350 portrait, 1440x1080 landscape, 1920x1080 landscape
Thumbnail: Displays at 400x300 pixels
Thumbnail file size: 500KB max

```html
<!DOCTYPE html>
<html lang="en">
<head>
<meta charset="utf-8">
<title>Dosewell – Unlimited PHCE Ceus ad set</title>
<link href="https://fonts.googleapis.com/css2?family=Poppins:wght@300;400;500;600;700&display=swap" rel="stylesheet">
<style>
  :root {
    --sheet-bg: #fbfcf8;
    --ad-bg: #ffffff;
    --cream: #fcf6ef;
    --navy: #1f3a5c;
    --blue: #1d6ea6;
    --green: #6aa241;
    --orange: #e58f35;
    --label: #3a3a3a;
    --muted: #6b7480;
    --figure-a: #2b8fc6;
    --figure-b: #55b9b6;
  }
  * { box-sizing: border-box; margin: 0; padding: 0; }
  html, body {
    width: 1200px; height: 1007px; overflow: hidden;
    background: var(--sheet-bg);
    font-family: "Poppins", sans-serif;
  }
  .sheet { position: relative; width: 1200px; height: 1007px; }

  .size-label {
    position: absolute; transform: translateX(-50%);
    font-size: 15px; font-weight: 300; color: var(--label);
    letter-spacing: 0.3px; line-height: 1;
  }

  .ad {
    position: absolute; overflow: hidden;
    background: var(--ad-bg);
    box-shadow: 0 6px 18px rgba(0,0,0,0.10);
  }
  .ad-backdrop { position: absolute; inset: 0; width: 100%; height: 100%; }

  .brand {
    position: absolute; transform: translate(-50%, -50%);
    display: flex; align-items: center; gap: 4px;
    font-weight: 600; color: var(--navy); font-size: 13px; line-height: 1; white-space: nowrap;
  }
  .brand-dot { width: 8px; height: 8px; border-radius: 50%; background: var(--green); }

  .offer-box {
    position: absolute; border: 1.5px solid var(--orange);
  }
  .offer-kicker {
    position: absolute; left: 0; right: 0; text-align: center;
    font-size: 10px; font-weight: 400; letter-spacing: 3.2px; color: var(--green);
    transform: translateY(-50%); line-height: 1;
  }
  .offer-title {
    position: absolute; left: 0; right: 0; text-align: center;
    font-size: 32px; font-weight: 700; color: var(--navy); letter-spacing: -0.5px;
    transform: translateY(-50%); line-height: 1; white-space: nowrap;
  }
  .offer-price {
    position: absolute; left: 50%; bottom: 0; transform: translate(-50%, 50%);
    padding: 0 6px; background: var(--ad-bg);
    font-size: 40px; font-weight: 600; color: var(--orange); line-height: 1;
  }

  .team-art {
    position: absolute; border-radius: 6px;
    background: linear-gradient(90deg, #e8f3fa 0%, var(--figure-a) 30%, #3f7fa0 50%, #1a6ca8 70%, var(--figure-b) 100%);
    opacity: 0.85;
  }

  .color-bar {
    position: absolute; left: 0; right: 0; height: 3px; display: flex;
  }
  .color-bar span { flex: 1; }
  .color-bar .navy { background: var(--navy); }
  .color-bar .blue { background: var(--blue); }
  .color-bar .green { background: var(--green); }
  .color-bar .orange { background: var(--orange); }

  .site-url {
    position: absolute; left: 0; right: 0; text-align: center;
    font-size: 5px; letter-spacing: 1.5px; color: var(--muted); transform: translateY(-50%);
  }

  /* Square 1080 x 1080 */
  .ad-square { left: 69px; top: 69px; width: 356px; height: 355px; }
  .ad-square .brand { left: 307px; top: 29px; }
  .ad-square .offer-box { left: 14px; top: 13px; width: 198px; height: 78px; }
  .ad-square .offer-kicker { top: 18px; }
  .ad-square .offer-title { top: 41px; }
  .ad-square .team-art { left: 17px; top: 126px; width: 337px; height: 200px; }
  .ad-square .color-bar { top: 339px; }
  .ad-square .site-url { top: 348px; }

  /* Landscape 1440 x 1080 */
  .ad-landscape { left: 498px; top: 69px; width: 475px; height: 355px; }
  .ad-landscape .brand { left: 424px; top: 31px; }
  .ad-landscape .offer-box { left: 19px; top: 18px; width: 199px; height: 78px; }
  .ad-landscape .offer-kicker { top: 18px; }
  .ad-landscape .offer-title { top: 41px; }
  .ad-landscape .team-art { left: 91px; top: 132px; width: 320px; height: 188px; }
  .ad-landscape .color-bar { top: 331px; }
  .ad-landscape .site-url { top: 344px; }

  /* Portrait 1080 x 1350 */
  .ad-portrait { left: 69px; top: 493px; width: 356px; height: 445px; }
  .ad-portrait .brand { left: 178px; top: 26px; }
  .ad-portrait .offer-box { left: 79px; top: 63px; width: 198px; height: 78px; }
  .ad-portrait .offer-kicker { top: 18px; }
  .ad-portrait .offer-title { top: 41px; }
  .ad-portrait .team-art { left: 17px; top: 184px; width: 334px; height: 217px; }
  .ad-portrait .color-bar { top: 419px; }
  .ad-portrait .site-url { top: 433px; }

  /* Widescreen 1920 x 1080 */
  .ad-wide { left: 498px; top: 493px; width: 632px; height: 356px; }
  .ad-wide .brand { left: 138px; top: 42px; font-size: 18px; }
  .ad-wide .brand-dot { width: 10px; height: 10px; }
  .ad-wide .offer-box { left: 19px; top: 87px; width: 239px; height: 94px; }
  .ad-wide .offer-kicker { top: 24px; font-size: 11px; }
  .ad-wide .offer-title { top: 53px; font-size: 33px; }
  .ad-wide .team-art { left: 277px; top: 50px; width: 355px; height: 248px; }
  .ad-wide .color-bar { top: 315px; }
  .ad-wide .site-url { top: 337px; font-size: 7px; letter-spacing: 2.5px; }
</style>
</head>
<body>
<main class="sheet">

  <span class="size-label" style="left:247px;top:40px">1080 x 1080</span>
  <span class="size-label" style="left:735px;top:40px">1440 x 1080</span>
  <span class="size-label" style="left:247px;top:465px">1080 x 1350</span>
  <span class="size-label" style="left:814px;top:465px">1920 x 1080</span>

  <section class="ad ad-square">
    <svg class="ad-backdrop" viewBox="0 0 356 355" preserveAspectRatio="none" aria-hidden="true">
      <path d="M0 200 C 20 140, 90 150, 160 170 C 230 190, 260 70, 356 68 L356 355 L0 355 Z" fill="var(--cream)"/>
    </svg>
    <div class="brand"><span>Dosewell</span><span class="brand-dot"></span></div>
    <div class="offer-box">
      <span class="offer-kicker">UNLIMITED</span>
      <span class="offer-title">PHCE Ceus</span>
      <span class="offer-price">$39</span>
    </div>
    <div class="team-art" role="img" aria-label="Illustration of four healthcare professionals: a doctor holding an X-ray, a doctor with a clipboard, a nurse in blue and a surgeon in teal scrubs giving a thumbs up"></div>
    <div class="color-bar"><span class="navy"></span><span class="blue"></span><span class="green"></span><span class="orange"></span></div>
    <p class="site-url">WWW.DOSEWELL.COM</p>
  </section>

  <section class="ad ad-landscape">
    <svg class="ad-backdrop" viewBox="0 0 475 355" preserveAspectRatio="none" aria-hidden="true">
      <path d="M55 355 C 40 250, 80 170, 170 165 C 260 160, 300 90, 380 95 C 430 98, 460 120, 475 140 L475 355 Z" fill="var(--cream)"/>
    </svg>
    <div class="brand"><span>Dosewell</span><span class="brand-dot"></span></div>
    <div class="offer-box">
      <span class="offer-kicker">UNLIMITED</span>
      <span class="offer-title">PHCE Ceus</span>
      <span class="offer-price">$39</span>
    </div>
    <div class="team-art" role="img" aria-label="Illustration of four healthcare professionals: a doctor holding an X-ray, a doctor with a clipboard, a nurse in blue and a surgeon in teal scrubs giving a thumbs up"></div>
    <div class="color-bar"><span class="navy"></span><span class="blue"></span><span class="green"></span><span class="orange"></span></div>
    <p class="site-url">WWW.DOSEWELL.COM</p>
  </section>

  <section class="ad ad-portrait">
    <svg class="ad-backdrop" viewBox="0 0 356 445" preserveAspectRatio="none" aria-hidden="true">
      <path d="M0 250 C 40 200, 130 200, 200 215 C 260 228, 290 160, 356 150 L356 445 L0 445 Z" fill="var(--cream)"/>
    </svg>
    <div class="brand"><span>Dosewell</span><span class="brand-dot"></span></div>
    <div class="offer-box">
      <span class="offer-kicker">UNLIMITED</span>
      <span class="offer-title">PHCE Ceus</span>
      <span class="offer-price">$39</span>
    </div>
    <div class="team-art" role="img" aria-label="Illustration of four healthcare professionals: a doctor holding an X-ray, a doctor with a clipboard, a nurse in blue and a surgeon in teal scrubs giving a thumbs up"></div>
    <div class="color-bar"><span class="navy"></span><span class="blue"></span><span class="green"></span><span class="orange"></span></div>
    <p class="site-url">WWW.DOSEWELL.COM</p>
  </section>

  <section class="ad ad-wide">
    <svg class="ad-backdrop" viewBox="0 0 632 356" preserveAspectRatio="none" aria-hidden="true">
      <path d="M265 356 C 255 260, 250 150, 330 110 C 400 75, 470 70, 520 40 C 570 10, 610 5, 632 8 L632 356 Z" fill="var(--cream)"/>
    </svg>
    <div class="brand"><span>Dosewell</span><span class="brand-dot"></span></div>
    <div class="offer-box">
      <span class="offer-kicker">UNLIMITED</span>
      <span class="offer-title">PHCE Ceus</span>
      <span class="offer-price">$39</span>
    </div>
    <div class="team-art" role="img" aria-label="Illustration of four healthcare professionals: a doctor holding an X-ray, a doctor with a clipboard, a nurse in blue and a surgeon in teal scrubs giving a thumbs up"></div>
    <div class="color-bar"><span class="navy"></span><span class="blue"></span><span class="green"></span><span class="orange"></span></div>
    <p class="site-url">WWW.DOSEWELL.COM</p>
  </section>

</main>
</body>
</html>
```